Regional Consulting Business Needs a Business Card Design

We need a business card design for our new business based in Regional Victoria, Australia called Velor Power. We are a consulting company with our main goal being to save people momey money and reducing their carbon footprint. Anything from water saving showerheads, to energy saving lightglobes and even to solar power. We would like to see designs that use bright colours. The final design should shout 'we are here to help you'.

Industry/Entity Type

Business

```html
<!DOCTYPE html>
<html lang="en">
<head>
<meta charset="utf-8">
<title>Velor Power – Business Card</title>
<link href="https://fonts.googleapis.com/css2?family=Roboto:wght@400;700&display=swap" rel="stylesheet">
<style>
  :root {
    --page-bg: #ecebe8;
    --card-bg: #ffffff;
    --charcoal: #434343;
    --amber: #f4a21b;
    --ink: #333333;
    --ink-soft: #555555;
    --on-dark: #ffffff;
  }
  * { margin: 0; padding: 0; box-sizing: border-box; }
  html, body {
    width: 1200px; height: 665px; overflow: hidden;
    background: var(--page-bg);
    font-family: "Roboto", Arial, sans-serif;
  }
  .stage {
    position: relative; width: 1200px; height: 665px;
    display: flex; align-items: center; justify-content: center; gap: 40px;
  }
  .card {
    position: relative; width: 540px; height: 309px;
    background: var(--card-bg);
    box-shadow: 0 4px 14px rgba(0,0,0,0.18);
    overflow: hidden;
  }
  .card-waves { position: absolute; left: 0; top: 0; width: 540px; height: 309px; }

  .brand { position: absolute; display: flex; align-items: center; gap: 14px; }
  .brand-mark { width: 44px; height: 44px; background: var(--amber); flex: none; }
  .brand-text { display: flex; flex-direction: column; }
  .brand-name { font-weight: 700; color: var(--charcoal); line-height: 1; }
  .brand-tagline { font-weight: 700; color: var(--ink); margin-top: 6px; }

  /* front */
  .card--front .brand { left: 40px; top: 40px; }
  .card--front .brand-name { font-size: 38px; }
  .card--front .brand-tagline { font-size: 15px; }

  .contact-list {
    position: absolute; right: 28px; top: 106px; list-style: none;
    font-size: 13px; color: var(--ink); line-height: 20px;
  }
  .contact-list li { display: flex; justify-content: flex-end; align-items: center; gap: 8px; }
  .contact-icon { width: 11px; height: 11px; fill: var(--amber); flex: none; }

  .person { position: absolute; left: 40px; top: 150px; }
  .person-name { font-size: 18px; font-weight: 700; color: var(--ink); }
  .person-title { font-size: 12px; color: var(--ink-soft); margin-top: 2px; }

  .address {
    position: absolute; left: 40px; bottom: 22px;
    font-size: 13px; color: var(--on-dark);
  }

  /* back */
  .card--back .brand { left: 30px; top: 70px; }
  .card--back .brand-mark { width: 60px; height: 60px; }
  .card--back .brand-name { font-size: 50px; }
  .card--back .brand-tagline { font-size: 18px; }
  .web-address {
    position: absolute; left: 48px; bottom: 70px;
    font-size: 15px; font-weight: 700; color: var(--on-dark);
  }
</style>
</head>
<body>
<main class="stage">

  <section class="card card--front" aria-label="Card front">
    <svg class="card-waves" viewBox="0 0 540 309" aria-hidden="true">
      <path d="M0 264 C130 226 280 226 380 228 C450 229 510 220 540 208 L540 309 L0 309 Z" fill="var(--charcoal)"/>
      <path d="M0 252 C130 214 280 214 380 216 C450 217 510 208 540 196" fill="none" stroke="var(--amber)" stroke-width="4"/>
    </svg>

    <div class="brand">
      <span class="brand-mark"></span>
      <div class="brand-text">
        <span class="brand-name">Velor Power</span>
        <span class="brand-tagline">Maintanence and consulting services</span>
      </div>
    </div>

    <ul class="contact-list">
      <li>555-014-2260
        <svg class="contact-icon" viewBox="0 0 12 12"><path d="M3 1l2 2-1 1.5c.8 1.5 2 2.7 3.5 3.5L9 7l2 2-1.5 2C5 10.5 1.5 7 1 2.5Z"/></svg>
      </li>
      <li>555-014-2261
        <svg class="contact-icon" viewBox="0 0 12 12"><circle cx="6" cy="3.5" r="2.5"/><path d="M1 11c0-3 2.2-4.5 5-4.5s5 1.5 5 4.5Z"/></svg>
      </li>
      <li>hello@velorpower.net
        <svg class="contact-icon" viewBox="0 0 12 12"><path d="M1 2.5h10v7H1Z"/><path d="M1 2.5l5 4 5-4" fill="none" stroke="#fff" stroke-width="1"/></svg>
      </li>
      <li>www.velorpower.net
        <svg class="contact-icon" viewBox="0 0 12 12"><circle cx="6" cy="6" r="5" fill="none" stroke="var(--amber)" stroke-width="1.4"/><circle cx="6" cy="6" r="2"/></svg>
      </li>
    </ul>

    <div class="person">
      <p class="person-name">Your Name</p>
      <p class="person-title">Title</p>
    </div>

    <p class="address">Street Name, City, State, zip code</p>
  </section>

  <section class="card card--back" aria-label="Card back">
    <svg class="card-waves" viewBox="0 0 540 309" aria-hidden="true">
      <path d="M0 212 C150 190 300 230 380 265 C440 290 500 292 540 288 L540 309 L0 309 Z" fill="var(--charcoal)"/>
      <path d="M0 200 C150 178 300 218 380 253 C440 278 500 280 540 276" fill="none" stroke="var(--amber)" stroke-width="4"/>
      <path d="M0 194 C150 172 300 212 380 247 C440 272 500 274 540 270" fill="none" stroke="var(--amber)" stroke-width="2"/>
    </svg>

    <div class="brand">
      <span class="brand-mark"></span>
      <div class="brand-text">
        <span class="brand-name">Velor Power</span>
        <span class="brand-tagline">Maintanence and consulting services</span>
      </div>
    </div>

    <p class="web-address">www.velorpower.net</p>
  </section>

</main>
</body>
</html>
```